Tarvel Ridge LLC

Need Professional Business cards for New Investment Fund

Target Market(s)

High Quality investors

Industry/Entity Type

Financial

Contact Information for Business Card

Phone Number +1 555 284 6193
Name Pavel Orlinsky
Title Fund Manager
email po@FundTarvel.example
Website www.FundTarvel.example

Colors

Designer to choose colors to be used in the design.

Requirements
Must have
• Must have our Logo and all of the above. Must be made so lettering and loge can be raised

```html
<!DOCTYPE html>
<html lang="en">
<head>
<meta charset="utf-8">
<title>Tarvel Ridge LLC – Business Card</title>
<link rel="stylesheet" href="https://fonts.googleapis.com/css2?family=Open+Sans:wght@400;600;700&display=swap">
<style>
  :root {
    --stage: #2d2f31;
    --card-green: #3e4a3e;
    --card-green-dark: #364136;
    --accent: #22e022;
    --paper: #ffffff;
    --paper-shade: #eef0ee;
    --ink-light: #e6ece6;
    --ink-muted: #c9d2c9;
    --brand-ink: #3e4a3e;
  }
  * { box-sizing: border-box; margin: 0; padding: 0; }
  html, body {
    width: 1200px; height: 1000px; overflow: hidden;
    background: var(--stage);
    font-family: "Open Sans", Arial, sans-serif;
  }
  .sheet {
    position: relative; width: 1200px; height: 1000px;
    display: flex; flex-direction: column; align-items: center; justify-content: center; gap: 60px;
  }
  .card {
    position: relative; width: 600px; height: 343px; overflow: hidden;
    box-shadow: 0 10px 28px rgba(0,0,0,.45);
  }

  /* Front */
  .card--front { display: flex; background: var(--paper); }
  .front__info {
    width: 55%; height: 100%; background: var(--card-green);
    padding: 78px 0 0 46px; color: var(--ink-light);
  }
  .holder__name {
    font-weight: 700; font-size: 21px; letter-spacing: .5px;
    color: var(--accent); text-transform: uppercase;
  }
  .holder__title { font-weight: 600; font-size: 13px; margin-top: 2px; color: var(--ink-light); }
  .contact-list { list-style: none; margin-top: 20px; }
  .contact-list li {
    display: flex; align-items: center; gap: 10px;
    font-size: 15px; color: var(--ink-muted); line-height: 23px;
  }
  .contact-list svg { width: 13px; height: 13px; flex: none; fill: var(--accent); }
  .front__brand {
    flex: 1; display: flex; align-items: center; justify-content: center; gap: 12px;
    background: linear-gradient(135deg, var(--paper) 40%, var(--paper-shade));
  }
  .brand-square { width: 18px; height: 18px; background: var(--accent); }
  .brand-name {
    font-weight: 700; font-size: 28px; letter-spacing: 1px;
    color: var(--brand-ink); text-transform: uppercase;
  }

  /* Back */
  .card--back { background: var(--card-green); }
  .back__pattern {
    position: absolute; inset: 0;
    background: linear-gradient(160deg, var(--card-green) 0%, var(--card-green-dark) 100%);
  }
  .back__brand {
    position: absolute; right: 34px; bottom: 40px;
    display: flex; align-items: center; gap: 8px;
  }
  .back__brand .brand-square { width: 12px; height: 12px; }
  .back__brand .brand-name { font-size: 15px; color: var(--paper); }
</style>
</head>
<body>
<main class="sheet">
  <section class="card card--front" aria-label="Business card front">
    <div class="front__info">
      <h1 class="holder__name">Pavel Orlinsky</h1>
      <p class="holder__title">Fund Manager</p>
      <ul class="contact-list">
        <li>
          <svg viewBox="0 0 16 16" aria-hidden="true"><path d="M3 1h3l1.5 4-2 1.3a9 9 0 0 0 4.2 4.2L11 8.5l4 1.5v3a2 2 0 0 1-2 2A13 13 0 0 1 1 3a2 2 0 0 1 2-2z"/></svg>
          +1 555 284 6193
        </li>
        <li>
          <svg viewBox="0 0 16 16" aria-hidden="true"><path d="M1 3h14v10H1z M1 3l7 6 7-6" fill="none" stroke="currentColor"/><path d="M1 3h14v1.2L8 10 1 4.2z"/><path d="M1 5.5l7 5.8 7-5.8V13H1z"/></svg>
          po@FundTarvel.example
        </li>
        <li>
          <svg viewBox="0 0 16 16" aria-hidden="true"><circle cx="8" cy="8" r="7"/><path d="M1 8h14M8 1c-3 3.5-3 10.5 0 14M8 1c3 3.5 3 10.5 0 14" stroke="#3e4a3e" stroke-width="1.2" fill="none"/></svg>
          www.FundTarvel.example
        </li>
      </ul>
    </div>
    <div class="front__brand">
      <span class="brand-square" aria-hidden="true"></span>
      <span class="brand-name">Tarvel Ridge</span>
    </div>
  </section>

  <section class="card card--back" aria-label="Business card back">
    <div class="back__pattern" role="img" aria-label="Raised repeating monogram pattern across the card back"></div>
    <div class="back__brand">
      <span class="brand-square" aria-hidden="true"></span>
      <span class="brand-name">Tarvel Ridge</span>
    </div>
  </section>
</main>
</body>
</html>
```